Business Report Cover

We need a revamped quarterly report cover to send to our clients. We asset manage commercial and residential properties throughout the the United States. We use a .pdf version of a cover that we've used for years but would like a fresh updated look for 2018. The cover should include our company logo (KOL Ventures) and a photo of the property as well as the Quarter/Year of the report.

Industry/Entity Type

Business

```html
<!DOCTYPE html>
<html lang="en">
<head>
<meta charset="utf-8">
<title>KOL Ventures – Quarterly Operating Report Cover</title>
<link rel="stylesheet" href="https://fonts.googleapis.com/css2?family=Jost:wght@400;500;600;700&family=Roboto:wght@300;400&display=swap">
<style>
  :root {
    --backdrop: #e6e6e6;
    --paper: #ffffff;
    --ink: #1b1b1b;
    --ink-soft: #3a3a3a;
    --title-panel: rgba(24, 52, 44, 0.93);
    --title-text: #ffffff;
    --rule: #555555;
    --sky-top: #3e7fd8;
    --sky-low: #9db6e2;
    --facade: #8a8470;
    --lights: #c9a24a;
    --water: #2b62a6;
    --water-deep: #183a78;
  }
  * { margin: 0; padding: 0; box-sizing: border-box; }
  html, body {
    width: 900px;
    height: 1200px;
    overflow: hidden;
    background: var(--backdrop);
  }
  .cover {
    position: absolute;
    left: 25px;
    top: 0;
    width: 677px;
    height: 956px;
    background: var(--paper);
    transform: scale(1.2552);
    transform-origin: top left;
    font-family: "Jost", "Futura", sans-serif;
    color: var(--ink);
  }
  .tagline {
    position: absolute;
    left: 45px;
    top: 83px;
    font-size: 17px;
    font-weight: 400;
    letter-spacing: 0.4px;
    color: var(--ink-soft);
    white-space: nowrap;
  }
  .property-photo {
    position: absolute;
    left: 0;
    top: 123px;
    width: 677px;
    height: 641px;
    background: linear-gradient(180deg,
      var(--sky-top) 0%,
      var(--sky-low) 22%,
      var(--facade) 42%,
      var(--lights) 62%,
      var(--water) 78%,
      var(--water-deep) 100%);
  }
  .title-panel {
    position: absolute;
    left: 28px;
    top: 123px;
    width: 298px;
    height: 297px;
    background: var(--title-panel);
    color: var(--title-text);
    padding: 38px 0 0 17px;
  }
  .report-title {
    font-size: 47px;
    font-weight: 500;
    line-height: 55px;
    letter-spacing: 0.5px;
  }
  .report-period {
    margin-top: 37px;
    font-size: 19px;
    font-weight: 400;
    letter-spacing: 0.3px;
    display: flex;
    align-items: center;
  }
  .report-period .divider {
    display: inline-block;
    width: 1.5px;
    height: 22px;
    background: var(--title-text);
    margin: 0 10px 0 12px;
  }
  .report-period .year { font-weight: 700; }
  .brand {
    position: absolute;
    left: 77px;
    top: 800px;
    width: 170px;
    font-family: "Jost", sans-serif;
    font-weight: 700;
    color: var(--ink);
    text-align: center;
  }
  .brand-name { font-size: 62px; line-height: 60px; letter-spacing: -1px; }
  .brand-sub { font-size: 15px; letter-spacing: 4.6px; margin-top: 2px; }
  .contact {
    position: absolute;
    left: 311px;
    top: 806px;
    width: 328px;
    font-style: normal;
  }
  .address {
    display: flex;
    align-items: flex-start;
    gap: 9px;
  }
  .address svg { margin-top: 3px; flex: none; }
  .address-text {
    font-family: "Roboto", sans-serif;
    font-style: normal;
    font-weight: 300;
    font-size: 15px;
    line-height: 19px;
    color: var(--ink-soft);
    white-space: nowrap;
  }
  .contact-rule {
    margin-top: 5px;
    height: 1px;
    background: var(--rule);
  }
  .social {
    display: flex;
    gap: 9px;
    margin-top: 12px;
    padding-left: 2px;
  }
  .social span {
    width: 13px;
    height: 13px;
    border-radius: 50%;
    background: var(--ink-soft);
  }
</style>
</head>
<body>
  <main class="cover">
    <p class="tagline">CORE VALUES DRIVE OUR SUCCESS, AND YOURS.</p>

    <div class="property-photo" role="img" aria-label="Photo of a lit waterfront apartment building at dusk, reflected in the water"></div>

    <section class="title-panel">
      <h1 class="report-title">QUARTERLY<br>OPERATING<br>REPORT</h1>
      <p class="report-period"><span>1ST QUARTER</span><span class="divider"></span><span class="year">2018</span></p>
    </section>

    <div class="brand">
      <div class="brand-name">KOL</div>
      <div class="brand-sub">VENTURES</div>
    </div>

    <address class="contact">
      <div class="address">
        <svg width="15" height="22" viewBox="0 0 15 22" aria-hidden="true">
          <path d="M7.5 0C3.4 0 0 3.3 0 7.4 0 12.6 7.5 22 7.5 22S15 12.6 15 7.4C15 3.3 11.6 0 7.5 0z" fill="#3a3a3a"/>
          <circle cx="7.5" cy="7.4" r="2.8" fill="#ffffff"/>
        </svg>
        <p class="address-text">Harbor Market, 4120 NW Lakeside<br>Commons Dr., Lakeport, WA 98000</p>
      </div>
      <div class="contact-rule"></div>
      <div class="social" aria-label="Social media links">
        <span></span><span></span><span></span>
      </div>
    </address>
  </main>
</body>
</html>
```